I have a logo and need to design the business card and stationery.
Updates

The uploaded logo image named as GREYMERE CONSTRUCTION which is to be replaced to GREYMERE CONTRACTS. Kindly add below details and submit the designs- Company name- Greymere Engineering Contracts LLP Name & Post- Vikrul Joshan (Designated Partner) Address- Block No.317, Wing C, Tolvan Trade Plaza, Kesar Marg Road, Nirmal Industrial Estate, Kandivli(E), Mumbai - 400 071 Contact- +91 97415 60829 Email- vikruljoshan@mailvora.example Website- www.greymerecontracts.example Contact for Letterhead- +91-22-28417753

Hi Tanvel Korim, We are liking your Design #28860835. We have suggested some changes which are mentioned in feedback. Kindly revert with it asap to finalize this design.

Colors

Designer to choose colors to be used in the design.

```html
<!DOCTYPE html>
<html lang="en">
<head>
<meta charset="utf-8">
<title>Greymere Contracts – Business Card</title>
<link rel="stylesheet" href="https://fonts.googleapis.com/css2?family=Arimo:wght@400;700&display=swap">
<style>
  :root {
    --backdrop: #9a9a9a;
    --card-white: #ffffff;
    --ink: #1e1e1e;
    --ink-soft: #5a5a5a;
    --rule: #3a3a3a;
    --card-dark: #2b2b2b;
    --pattern-light: #4a4a4a;
    --pattern-dark: #1c1c1c;
    --mark-white: #ffffff;
  }
  * { margin: 0; padding: 0; box-sizing: border-box; }
  html, body {
    width: 1200px; height: 800px; overflow: hidden;
    background: var(--backdrop);
    font-family: "Arimo", Arial, sans-serif;
  }
  .stage {
    position: relative; width: 1200px; height: 800px;
  }
  .card {
    position: absolute; top: 252px;
    width: 520px; height: 297px;
    box-shadow: 0 10px 24px rgba(0,0,0,0.25);
  }
  /* Front */
  .card-front { left: 50px; background: var(--card-white); }
  .brand {
    position: absolute; left: 40px; top: 0; width: 200px; height: 297px;
    display: flex; flex-direction: column; align-items: center; justify-content: center;
  }
  .brand-square {
    width: 58px; height: 58px; border: 7px solid var(--ink); margin-bottom: 14px;
  }
  .brand-name {
    font-weight: 400; color: var(--ink); font-size: 17px;
    letter-spacing: 3px; text-align: center; line-height: 1.35;
  }
  .divider {
    position: absolute; left: 268px; top: 98px; width: 1px; height: 118px;
    background: var(--rule);
  }
  .details {
    position: absolute; left: 290px; top: 94px; color: var(--ink-soft);
    font-size: 11.5px; line-height: 1.35;
  }
  .person-name { font-weight: 700; color: var(--ink); font-size: 17px; letter-spacing: 0.5px; }
  .person-title { margin-bottom: 10px; }
  .address { margin-bottom: 10px; }
  .contact-list { list-style: none; }
  .contact-list li { display: flex; align-items: center; gap: 7px; }
  .contact-list svg { width: 9px; height: 9px; flex: none; }
  /* Back */
  .card-back {
    left: 630px; background: var(--card-dark); overflow: hidden;
  }
  .pattern-field {
    position: absolute; inset: 0;
    background: linear-gradient(135deg, var(--pattern-light) 0%, var(--card-dark) 50%, var(--pattern-dark) 100%);
  }
  .back-mark {
    position: absolute; right: 44px; bottom: 58px;
    display: flex; align-items: center; gap: 10px;
    color: var(--mark-white); font-size: 12px; letter-spacing: 2px; font-weight: 400;
  }
  .back-mark-square { width: 22px; height: 22px; border: 3px solid var(--mark-white); }
</style>
</head>
<body>
<main class="stage">
  <section class="card card-front">
    <div class="brand">
      <div class="brand-square"></div>
      <div class="brand-name">GREYMERE<br>CONTRACTS</div>
    </div>
    <div class="divider"></div>
    <div class="details">
      <div class="person-name">ARLEN VOSS</div>
      <div class="person-title">President</div>
      <div class="address">4162 Larkfield Lane<br>Wrenford, Dalmere 58213</div>
      <ul class="contact-list">
        <li><svg viewBox="0 0 10 10" aria-hidden="true"><path d="M2 1 L4 1 L4.6 3 L3.4 3.8 Q4.4 5.8 6.2 6.6 L7 5.4 L9 6 L9 8 Q5 9 1.6 5 Q1 3 2 1Z" fill="#1e1e1e"/></svg>482-306-7719</li>
        <li><svg viewBox="0 0 10 10" aria-hidden="true"><rect x="1.5" y="1" width="7" height="8" rx="1" fill="none" stroke="#1e1e1e" stroke-width="1.2"/></svg>482-630-1974</li>
        <li><svg viewBox="0 0 10 10" aria-hidden="true"><rect x="0.8" y="2" width="8.4" height="6" fill="#1e1e1e"/><path d="M0.8 2 L5 5.5 L9.2 2" fill="none" stroke="#fff" stroke-width="0.8"/></svg>name@greymere.example</li>
        <li><svg viewBox="0 0 10 10" aria-hidden="true"><circle cx="5" cy="5" r="4.2" fill="#1e1e1e"/><path d="M0.8 5 H9.2 M5 0.8 Q2.5 5 5 9.2 M5 0.8 Q7.5 5 5 9.2" fill="none" stroke="#fff" stroke-width="0.6"/></svg>www.greymere.example</li>
      </ul>
    </div>
  </section>

  <section class="card card-back">
    <div class="pattern-field" role="img" aria-label="Embossed repeating brand pattern across the dark card back"></div>
    <div class="back-mark">
      <div class="back-mark-square"></div>
      <span>GREYMERE CONTRACTS</span>
    </div>
  </section>
</main>
</body>
</html>
```